Nutritional Supplement Brand in Need of a Website Cleanse!

We are in need of a website overhaul, one that will make our product, which is a healthy greens powder supplement, appear more sophisticated and appealing. Up till now most of our efforts have focused on formulating the product and setting up distribution. We did go down the internet marketing / pagetrailz selling path without too much success. What we'd like to do now is really bring focus to the benefits of the product, the ingredients, the value proposition. We would like green designs that accentuate the healthy energy and benefits the product drives (a very fresh, clean and energetic feel).
Updates

Project Deadline Extended
Reason: Extending the deadline out 5 days since I was late in providing feedback and because so many great designs were submitted. Thanks for your patience and understanding.

Target Market(s)

People who suffer from low energy levels and those who live a very active lifestyle and are in search of ways to boost their energy in a healthy way (not through coffee or sugary energy drinks). Primarily M/F in the 25-45 age range. Also people who know that they need to eat more fruits and vegetables on a daily basis but have neither the time or the money to do so.

Industry/Entity Type

Health And Wellness

Number of Pages Required

1 page

Font styles to use
Sans Serif

Colors
cadf82
acd036
b5d664
eaf2ce

Requirements
Must have
• My site is currently in Wordpress and can be seen at http://www.verdalux27blend.com
• The product can also be found on Shopvarro at https://www.shopvarro.com/dp/K47QWMZRX2
• I would like the site to remain in Wordpress and will pay extra to have the layout coded into Wordpress although this isn't a requirement for proposals.
• Here are some examples of sites around my niche that I like the look and feel of:
• http://www.plenivo.com/2-classic-cb/
• https://sprintleafusa.com/
• https://www.brisklawn.com/
• http://velaroot.com/turmeric/
• My current site is in the layout of a long-form sales letter. I don't want the new design to be so sales-pitch in manner. I want it to be more about the energy-driving benefits of the core ingredients in the formula and testimonials (designs can leverage some that are on my existing site and positive reviews on the Shopvarro listing). My current site leads with a video but this is not necessary in the redesign. I do have an edited video that's 2-3 minutes long that could be leveraged if a designer wanted to go down this path (it's absolutely not necessary though). I plan to utilize social media influencers to drive traffic to my listing so I'm hoping this will allow for a bit less sales-pitch needed on the site itself. Using all of the copy that's on the existing website in not necessary, a lot of it is redundant and it's in need of an overhaul. I'd rather slim down the site and keep it very product-focused.
• In terms of social media I'd like a link to my instagram and facebook pages:
• https://www.instagram.com/verdalux27blend/
• https://www.facebook.com/V27Blend/
• I want the site to be responsive and look great on all devices (desktop, mobile).
• I'm new to artjostle so please hit me up with further questions if needed.
Nice to have
• Would love a new look and feel to my logo. I'm not a huge fan of the current one. I can't really change the name of the product at this point but the logo on the site can be edited and a new look is encouraged.

```html
<!DOCTYPE html>
<html lang="en">
<head>
<meta charset="utf-8">
<title>Verdalux 27 Blend – Natural Everyday Energy</title>
<link href="https://fonts.googleapis.com/css2?family=Oswald:wght@400;500;700&family=Open+Sans:wght@400;600;700&display=swap" rel="stylesheet">
<style>
:root{
  --lime:#acd036;
  --lime-soft:#b5d664;
  --lime-pale:#cadf82;
  --mint:#eaf2ce;
  --ink:#1c1c1c;
  --charcoal:#222;
  --text:#555;
  --grey-bg:#f4f4f4;
  --white:#fff;
  --orange:#ef6b1f;
  --blue:#1f8fd6;
  --red:#d7262b;
}
*{box-sizing:border-box;margin:0;padding:0}
html,body{width:1200px;height:4986px;overflow:hidden}
body{font-family:'Open Sans',sans-serif;color:var(--text);background:var(--white);font-size:13px;line-height:1.6}
h1,h2,h3,h4,.nav a,.btn{font-family:'Oswald',sans-serif}
section{position:relative;overflow:hidden}
.wrap{position:absolute;top:0;left:50%;margin-left:-500px;width:1000px;height:100%}
.btn{display:inline-block;background:var(--ink);color:var(--white);font-size:12px;letter-spacing:.5px;padding:12px 22px;text-transform:uppercase;text-decoration:none}
.btn-lime{background:var(--lime);color:var(--white);font-size:12px;padding:8px 24px}
.ph{display:block}
.more{color:var(--lime);font-weight:700;font-size:12px;text-decoration:none}

/* header */
.topbar{position:relative;height:150px;background:var(--charcoal)}
.brand{position:absolute;left:40px;top:22px;display:flex;align-items:center;gap:12px}
.brand-dot{width:64px;height:64px;border-radius:50%;background:var(--lime)}
.brand-name{font-family:'Oswald',sans-serif;font-weight:700;color:var(--white);font-size:26px;line-height:1}
.guarantee{position:absolute;right:40px;top:44px;display:flex;align-items:center;gap:16px}
.guarantee p{font-family:'Oswald',sans-serif;color:var(--white);font-size:24px;letter-spacing:.5px}
.guarantee b{color:var(--lime);font-size:34px}
.seal{width:66px;height:66px;border-radius:50%;background:#d9a92a}

.nav{height:50px;background:var(--white);border-bottom:1px solid #e5e5e5}
.nav ul{list-style:none;display:flex;justify-content:space-between;width:1000px;margin:0 auto;height:50px}
.nav li{height:50px}
.nav a{display:block;line-height:50px;padding:0 32px;color:var(--lime);font-size:13px;text-decoration:none}
.nav .active a{background:var(--lime);color:var(--white)}

/* hero */
.hero{height:548px;background:linear-gradient(180deg,var(--mint),#dcebb2)}
.hero-copy{position:absolute;left:30px;top:128px;width:520px}
.hero-copy h3{font-size:34px;font-weight:400;color:var(--ink)}
.hero-copy h1{font-size:64px;font-weight:700;color:var(--lime);line-height:1.1;margin-bottom:12px}
.hero-copy p{font-size:18px;color:var(--ink);margin-bottom:26px;line-height:1.55}
.hero-tubs{position:absolute;right:10px;top:40px;width:430px;height:470px}
.arrow{position:absolute;top:240px;width:20px;height:40px}

/* about */
.about{height:482px}
.about-photo{position:absolute;left:30px;top:110px;width:270px;height:270px;border-radius:50%;border:8px solid var(--lime);background:linear-gradient(135deg,#3a3a3a,#111)}
.about-copy{position:absolute;left:370px;top:130px;width:630px}
.about-copy h2{font-size:24px;color:var(--ink);font-weight:500;line-height:1.4;margin-bottom:22px}
.about-copy p{margin-bottom:16px}
.about-copy .caps{font-weight:700;color:var(--ink);font-size:12px}

/* symptoms */
.symptoms{height:490px;background:var(--grey-bg)}
.section-title{position:absolute;left:0;right:0;top:62px;text-align:center;font-size:26px;color:var(--ink);font-weight:500;line-height:1.3}
.grid4{position:absolute;left:20px;top:150px;width:960px;display:flex;justify-content:space-between}
.card{width:210px;text-align:center}
.circle{width:130px;height:130px;border-radius:50%;border:6px solid var(--white);margin:0 auto 18px;box-shadow:0 2px 6px rgba(0,0,0,.15)}
.card h4{font-size:12px;color:var(--ink);font-weight:500;margin-bottom:6px}
.card p{font-size:11px;line-height:1.55;margin-bottom:8px}

/* dark band */
.darkband{height:168px;background:var(--ink);text-align:center;padding-top:30px}
.darkband h3{color:var(--white);font-size:26px;font-weight:400}
.darkband h2{color:var(--lime);font-size:30px;font-weight:500}
.darkband p{color:#ccc;font-size:14px}

/* product feature */
.feature{height:488px}
.feature-copy{position:absolute;left:30px;top:100px;width:540px}
.feature-copy h2{font-size:28px;color:var(--ink);font-weight:500;margin-bottom:16px}
.feature-copy p{font-size:12px;margin-bottom:12px}
.feature-tub{position:absolute;right:40px;top:70px;width:260px;height:330px}

/* feedback */
.feedback{height:284px;background:linear-gradient(90deg,#9dc52a,var(--lime) 50%,#9dc52a)}
.feedback h2{text-align:center;color:var(--white);font-size:30px;font-weight:500;padding-top:60px}
.feedback p{width:560px;margin:16px auto 0;text-align:center;color:var(--white);font-size:12px}

/* usa */
.usa{height:465px}
.usa-tub{position:absolute;left:30px;top:70px;width:300px;height:320px}
.usa-copy{position:absolute;left:420px;top:100px;width:580px}
.usa-copy h2{font-size:28px;color:var(--ink);font-weight:500;margin-bottom:14px}
.usa-copy p{font-size:12px;margin-bottom:12px}

/* ingredients */
.ingredients{height:531px;background:var(--grey-bg)}
.ingredients .grid4{left:80px;width:840px;top:140px}
.ingredients .circle{width:150px;height:150px}
.slide{position:absolute;top:200px;width:34px;height:34px;border-radius:50%;background:#ddd}

/* different */
.different{height:464px}
.diff-copy{position:absolute;left:30px;top:90px;width:560px}
.diff-copy h2{font-size:28px;color:var(--ink);font-weight:500;line-height:1.25;margin-bottom:18px}
.ticks{list-style:none;margin-bottom:18px}
.ticks li{display:flex;align-items:center;gap:12px;font-size:12px;margin-bottom:8px}
.ticks svg{flex:none}
.facts{position:absolute;right:60px;top:50px;width:260px;height:340px}

/* pricing */
.pricing{height:632px;background:var(--lime-soft)}
.pricing h2{position:absolute;left:0;right:0;top:58px;text-align:center;color:var(--ink);font-size:28px;font-weight:500}
.plans{position:absolute;left:30px;top:140px;width:940px;display:flex;justify-content:space-between}
.plan{width:290px;height:440px;background:var(--white);text-align:center;box-shadow:0 3px 10px rgba(0,0,0,.15)}
.plan h3{color:var(--white);font-size:22px;font-weight:500;line-height:52px}
.silver h3{background:var(--orange)}.gold h3{background:var(--blue)}.platinum h3{background:var(--red)}
.plan .sub{font-size:13px;color:var(--ink);margin:14px 0 10px}
.plan .shot{width:120px;height:150px;margin:0 auto 14px}
.price{font-size:22px;color:var(--ink);font-weight:700;border-top:1px solid #eee;padding-top:10px}
.price span{font-size:12px;color:var(--text);font-weight:400}
.plan .note{font-size:12px;margin-bottom:14px}
.cards{display:flex;justify-content:center;gap:6px;margin-top:14px}
.cards i{display:block;width:30px;height:18px;border-radius:3px;background:#d8d8d8}

/* footer */
.footer{height:234px;text-align:center;padding-top:50px}
.social{display:flex;justify-content:center;gap:12px;margin-bottom:22px}
.social i{display:block;width:28px;height:28px;border-radius:50%;background:var(--blue)}
.social i:nth-child(3){background:var(--orange)}
.social i:nth-child(4){background:var(--lime)}
.footnav{font-size:11px;color:var(--ink);margin-bottom:8px}
.copy{font-size:11px}
</style>
</head>
<body>

<header class="topbar">
  <div class="brand"><span class="brand-dot"></span><span class="brand-name">VERDALUX<br>27 BLEND</span></div>
  <div class="guarantee"><p><b>60</b> DAY RISK FREE MONEY BACK GUARANTEE</p><span class="seal"></span></div>
</header>

<nav class="nav">
  <ul>
    <li class="active"><a href="#">HOME</a></li>
    <li><a href="#">ABOUT US</a></li>
    <li><a href="#">SERVICES</a></li>
    <li><a href="#">PRODUCTS</a></li>
    <li><a href="#">PRICING</a></li>
    <li><a href="#">BLOG</a></li>
    <li><a href="#">CONTACT US</a></li>
  </ul>
</nav>

<section class="hero">
  <svg class="arrow" style="left:60px" viewBox="0 0 20 40"><path d="M16 4 4 20l12 16" fill="none" stroke="#c3d98a" stroke-width="3"/></svg>
  <svg class="arrow" style="right:60px" viewBox="0 0 20 40"><path d="M4 4l12 16L4 36" fill="none" stroke="#c3d98a" stroke-width="3"/></svg>
  <div class="wrap">
    <div class="hero-copy">
      <h3>COMPLETELY NATURAL ENERGY TO</h3>
      <h1>POWER YOUR DAY</h1>
      <p>Delivers All Day Energy Without Side Effects and All Your Daily Servings Of Fruits and Veggies Easily...</p>
      <a class="btn" href="#">Click View More Information</a>
    </div>
    <svg class="hero-tubs ph" role="img" aria-label="Three tubs of Verdalux 27 Blend greens powder" viewBox="0 0 480 500">
      <defs><linearGradient id="tub" x1="0" x2="1"><stop offset="0" stop-color="#111"/><stop offset=".5" stop-color="#333"/><stop offset="1" stop-color="#111"/></linearGradient></defs>
      <rect x="20" y="70" width="150" height="380" rx="8" fill="url(#tub)"/>
      <rect x="310" y="70" width="150" height="380" rx="8" fill="url(#tub)"/>
      <rect x="110" y="20" width="260" height="470" rx="10" fill="url(#tub)"/>
      <rect x="130" y="160" width="220" height="140" fill="#7fb21f" opacity=".55"/>
    </svg>
  </div>
</section>

<section class="about">
  <div class="wrap">
    <div class="about-photo" role="img" aria-label="Athlete training with heavy ropes"></div>
    <div class="about-copy">
      <h2>THE COMPLETE NATURAL EVERYDAY ENERGY SUPPLEMENT<br>FOR PEOPLE ON THE GO</h2>
      <p>From now on, you don't have to settle for just a few hours of energy. And you can forget about taking separate supplements for overall health, well-being and the hassle of getting your daily fruits, vegetables and healthy foods, especially when you're on the go.</p>
      <p class="caps">ONE NEW SUPPLEMENT DOES EVERYTHING AND KEEPS YOU ENERGIZED ALL DAY LONG! KEEP READING TO DISCOVER THE SECRET!</p>
    </div>
  </div>
</section>

<section class="symptoms">
  <h2 class="section-title">DO THESE SYMPTOMS SOUND FAMILIAR TO YOU?</h2>
  <div class="wrap">
    <div class="grid4">
      <div class="card"><div class="circle" role="img" aria-label="Tired woman struggling to focus" style="background:linear-gradient(135deg,#b9b2a8,#6d645b)"></div>
        <h4>IT'S DIFFICULT TO STAY FOCUSED</h4><p>When in fact, many people can't get a good night's sleep because they are loaded up with harmful...</p><a class="more" href="#">Read More &gt;</a></div>
      <div class="card"><div class="circle" role="img" aria-label="Exhausted man resting on a desk" style="background:linear-gradient(135deg,#c9a98a,#5c4636)"></div>
        <h4>YOU GET TIRED REGULARLY</h4><p>You just can seem to keep your energy levels as high as you would like and get everything done...</p><a class="more" href="#">Read More &gt;</a></div>
      <div class="card"><div class="circle" role="img" aria-label="Woman feeling low on energy" style="background:linear-gradient(135deg,#d6c6b3,#7c6a58)"></div>
        <h4>YOU SUFFER FROM WORK-FATIGUE</h4><p>You struggle to get work done during the day and you are always reaching for more coffee or...</p><a class="more" href="#">Read More &gt;</a></div>
      <div class="card"><div class="circle" role="img" aria-label="Man rubbing his eyes from mental fatigue" style="background:linear-gradient(135deg,#cdbba6,#5e5246)"></div>
        <h4>YOU FEEL MENTAL FATIGUE</h4><p>The demands on you are enormous, and you often find yourself extremely tired from pressures at...</p><a class="more" href="#">Read More &gt;</a></div>
    </div>
  </div>
</section>

<section class="darkband">
  <h3>AND HERE'S POSSIBLY THE WORST PART:</h3>
  <h2>NO ONE REALLY UNDERSTANDS WHAT YOU'RE GOING THROUGH.</h2>
  <p>They may even get annoyed with you because you never seem to have enough energy.</p>
</section>

<section class="feature">
  <div class="wrap">
    <div class="feature-copy">
      <h2>VERDALUX 27 BLEND</h2>
      <p>Customers report that it works fast, it's completely guaranteed, and the price is completely reasonable. This is a major breakthrough for people suffering from low energy levels.</p>
      <p>But chances are, you've never heard of it. Because that's the way the big pharmaceutical companies want it. They spend over 50 billion dollars a year to advertise their products to the public and doctors.</p>
      <p>They have teams of sales people visiting doctors' offices daily to make sure they keep pushing their pills and prescriptions. So I understand most people haven't heard of Verdalux 27 Blend. That's the way the big drug companies want it. But let me assure you.</p>
      <a class="btn" href="#" style="margin-top:14px">Click View More Information</a>
    </div>
    <svg class="feature-tub ph" role="img" aria-label="Tub of Verdalux 27 Blend" viewBox="0 0 260 330"><rect x="20" y="0" width="220" height="330" rx="10" fill="url(#tub)"/><rect x="40" y="110" width="180" height="100" fill="#7fb21f" opacity=".55"/></svg>
  </div>
</section>

<section class="feedback" role="img" aria-label="Collage of happy customer portraits tinted green">
  <h2>THE FEEDBACK HAS BEEN INCREDIBLE</h2>
  <p>"We have been amazed reading these and our members have been more than thrilled with how quickly the results show. Many people say they finally have the energy to keep up with their kids again and their afternoons are productive. It's the feedback that keeps us going every day and helps so many others try it for themselves today."</p>
</section>

<section class="usa">
  <div class="wrap">
    <svg class="usa-tub ph" role="img" aria-label="Back of the Verdalux 27 Blend tub with label" viewBox="0 0 300 320"><rect x="30" y="0" width="240" height="320" rx="10" fill="#f2f2f2" stroke="#ddd"/><rect x="50" y="40" width="110" height="240" fill="#222"/><rect x="170" y="40" width="80" height="240" fill="#e3e3e3"/></svg>
    <div class="usa-copy">
      <h2>VERDALUX 27 BLEND IS 100% MADE IN THE USA</h2>
      <p>Most people aren't aware of it, but the ingredients of most vitamins and supplements today come from overseas. Even if the product says "Made in the USA," the actual ingredients may come from elsewhere or from farms with lower standards.</p>
      <p>You have no guarantee about the purity or quality of these ingredients. It's like a game of chance. Sooner or later, that gun is going to go off... and you don't want it pointing at you when it happens.</p>
      <p>None of our ingredients come from overseas. They are 100% sourced in the USA. Nearly all our ingredients are whole food and grown without pesticides, carefully harvesting the plants from their natural state.</p>
      <a class="btn" href="#" style="margin-top:10px">Click View More Information</a>
    </div>
  </div>
</section>

<section class="ingredients">
  <h2 class="section-title">OUR 8 NATURAL, MIRACLE INGREDIENTS INCLUDE</h2>
  <div class="wrap">
    <span class="slide" style="left:10px"></span><span class="slide" style="right:10px"></span>
    <div class="grid4">
      <div class="card"><div class="circle" role="img" aria-label="Spirulina powder in a bowl" style="background:radial-gradient(#8bb34a,#3f6a1c)"></div>
        <h4>SPIRULINA</h4><p>Spirulina has been called the most superior plant protein in the world. It is high in iron, calcium...</p><a class="more" href="#">Read More &gt;</a></div>
      <div class="card"><div class="circle" role="img" aria-label="Chlorella tablets and leaves" style="background:radial-gradient(#9ac455,#406b1f)"></div>
        <h4>CHLORELLA</h4><p>A green algae super high in protein and healthy polyunsaturated fats. Popular in Australia, it been...</p><a class="more" href="#">Read More &gt;</a></div>
      <div class="card"><div class="circle" role="img" aria-label="Fresh kelp seaweed" style="background:radial-gradient(#7fa33f,#2f4f17)"></div>
        <h4>KELP</h4><p>An excellent source of vitamins and minerals. Kelp has been shown to contain 46 minerals...</p><a class="more" href="#">Read More &gt;</a></div>
      <div class="card"><div class="circle" role="img" aria-label="Alfalfa sprouts" style="background:radial-gradient(#a4b86a,#4d5a2a)"></div>
        <h4>ALFALFA TRACE MINERAL</h4><p>Alfalfa has been used by the Chinese since the 6th century to treat several health conditions...</p><a class="more" href="#">Read More &gt;</a></div>
    </div>
  </div>
</section>

<section class="different">
  <div class="wrap">
    <div class="diff-copy">
      <h2>HOW VERDALUX 27 BLEND IS DIFFERENT<br>FROM OTHER PRODUCTS</h2>
      <ul class="ticks">
        <li><svg width="18" height="18" viewBox="0 0 18 18"><circle cx="9" cy="9" r="9" fill="#acd036"/><path d="M5 9.5l3 3 5-6" fill="none" stroke="#fff" stroke-width="2"/></svg>Actually Tastes Like Something You Could Drink Daily</li>
        <li><svg width="18" height="18" viewBox="0 0 18 18"><circle cx="9" cy="9" r="9" fill="#acd036"/><path d="M5 9.5l3 3 5-6" fill="none" stroke="#fff" stroke-width="2"/></svg>100% All Natural and 100% Made in the USA</li>
        <li><svg width="18" height="18" viewBox="0 0 18 18"><circle cx="9" cy="9" r="9" fill="#acd036"/><path d="M5 9.5l3 3 5-6" fill="none" stroke="#fff" stroke-width="2"/></svg>Equals the Nutritional Equivalent of 20 Servings of Fruits and Vegetables Daily</li>
        <li><svg width="18" height="18" viewBox="0 0 18 18"><circle cx="9" cy="9" r="9" fill="#acd036"/><path d="M5 9.5l3 3 5-6" fill="none" stroke="#fff" stroke-width="2"/></svg>Ok Completely Safe to Take Daily (Some Even Take 2x/Day)</li>
        <li><svg width="18" height="18" viewBox="0 0 18 18"><circle cx="9" cy="9" r="9" fill="#acd036"/><path d="M5 9.5l3 3 5-6" fill="none" stroke="#fff" stroke-width="2"/></svg>Contains 60 Ingredients Including Whole Food Sourced Fruits, Vegetables, Superfoods, Enzymes and...</li>
      </ul>
      <a class="btn" href="#">Click View More Information</a>
    </div>
    <svg class="facts ph" role="img" aria-label="Supplement facts label on the tub" viewBox="0 0 260 340"><rect width="260" height="340" rx="10" fill="#f2f2f2" stroke="#ddd"/><rect x="30" y="30" width="200" height="280" fill="#fff" stroke="#333" stroke-width="2"/></svg>
  </div>
</section>

<section class="pricing">
  <h2>PRICING PACKAGE</h2>
  <div class="wrap">
    <div class="plans">
      <div class="plan silver"><h3>SILVER</h3><p class="sub">Verdalux 27 Blend Single Bottle</p>
        <div class="shot" role="img" aria-label="One tub" style="background:linear-gradient(90deg,#111,#333,#111)"></div>
        <p class="price">$49.95 + <span>FREE SHIPPING</span></p><p class="note">Get one Bottle of Verdalux 27 Blend</p>
        <a class="btn btn-lime" href="#">ADD TO CART</a><div class="cards"><i></i><i></i><i></i><i></i></div></div>
      <div class="plan gold"><h3>GOLD</h3><p class="sub">3 Months Supply of Verdalux 27 Blend</p>
        <div class="shot" role="img" aria-label="Three tubs" style="background:linear-gradient(90deg,#111,#333,#111)"></div>
        <p class="price">129.95 + <span>FREE SHIPPING</span></p><p class="note">43.31 per Bottle</p>
        <a class="btn btn-lime" href="#">ADD TO CART</a><div class="cards"><i></i><i></i><i></i><i></i></div></div>
      <div class="plan platinum"><h3>PLATINUM</h3><p class="sub">4 Months Supply of Verdalux 27 Blend</p>
        <div class="shot" role="img" aria-label="Four tubs" style="background:linear-gradient(90deg,#eee,#fff,#ddd)"></div>
        <p class="price">149.95 + <span>FREE SHIPPING</span></p><p class="note">Only 37.48 per Bottle</p>
        <a class="btn btn-lime" href="#">ADD TO CART</a><div class="cards"><i></i><i></i><i></i><i></i></div></div>
    </div>
  </div>
</section>

<footer class="footer">
  <div class="social"><i></i><i></i><i></i><i></i><i></i></div>
  <p class="footnav">HOME | ABOUT US | SERVICES | PRODUCTS | PRICING | BLOG | CONTACT US</p>
  <p class="copy">COPYRIGHT © VERDALUX27BLEND.COM, 2017 | ALL RIGHTS RESERVED</p>
</footer>

</body>
</html>
```